BRIGHTDOOR7 - business card, letterhead and envelopes
BRIGHTDOOR7 - Business cards, letterhead and envelopes
Professional
BRIGHTDOOR7 LLC
Real Estate Solution Provider
info@brightdoor7.example
www.brightdoor7.example
We specialize in creative real estate solutions
We pay cash for houses!
We prevent foreclosures !
We help repair credit!
We pay referral fees!

```html
<!DOCTYPE html>
<html lang="en">
<head>
<meta charset="utf-8">
<title>BRIGHTDOOR7 – Business Card</title>
<link rel="stylesheet" href="https://fonts.googleapis.com/css2?family=Open+Sans:wght@400;600;700&display=swap">
<style>
  :root {
    --stage: #e6e8e3;
    --card-dark: #0c0c0e;
    --card-mid: #26262b;
    --gold: #e0a53a;
    --gold-light: #f6d27a;
    --gold-deep: #a86d16;
    --royal: #2e4ba8;
    --ink-light: #f1f1f1;
    --ink-muted: #c9c9c9;
  }
  * { box-sizing: border-box; margin: 0; padding: 0; }
  html, body {
    width: 1200px; height: 901px; overflow: hidden;
    background: var(--stage);
    font-family: "Open Sans", Arial, sans-serif;
  }
  .card {
    position: absolute; left: 250px; width: 700px; height: 400px;
    background: radial-gradient(ellipse at 40% 30%, var(--card-mid) 0%, var(--card-dark) 70%);
    border-radius: 6px;
    box-shadow: 0 12px 28px rgba(0,0,0,.28);
    overflow: hidden;
    color: var(--ink-light);
  }
  .card--front { top: 40px; }
  .card--back { top: 461px; }

  .brand {
    position: absolute; top: 78px; left: 0; right: 0;
    text-align: center;
  }
  .brand__name {
    display: inline-flex; align-items: center; gap: 12px;
    font-weight: 700; font-size: 46px; letter-spacing: 2px;
    color: var(--gold);
  }
  .brand__dot {
    width: 14px; height: 14px; border-radius: 50%; background: var(--gold);
  }
  .brand__tagline {
    margin-top: 6px; font-size: 17px; letter-spacing: 4px; color: var(--ink-light);
  }

  .contact {
    position: absolute; top: 210px; left: 0; right: 0;
    display: flex; justify-content: center; font-size: 17px; line-height: 1.5;
    color: var(--ink-muted);
  }
  .contact__address { text-align: right; padding-right: 26px; }
  .contact__lines { padding-left: 26px; border-left: 1px solid #666; }

  .site-band {
    position: absolute; left: 0; right: 0; bottom: 18px; height: 44px;
    border-top: 2px solid var(--royal);
    display: flex; align-items: center; justify-content: center;
    font-size: 15px; letter-spacing: 5px; color: var(--gold-light);
  }
  .gold-edge {
    position: absolute; left: 0; right: 0; bottom: 0; height: 18px;
    background: linear-gradient(90deg, var(--gold-deep), var(--gold-light) 50%, var(--gold-deep));
  }

  .services { position: absolute; top: 120px; left: 80px; right: 60px; }
  .services__title {
    font-weight: 700; font-size: 24px; color: var(--ink-light);
    padding-bottom: 14px; margin-bottom: 16px;
    border-bottom: 2px solid var(--gold);
  }
  .services__list { list-style: none; font-size: 24px; line-height: 1.4; color: var(--ink-light); }
  .accent-bar {
    position: absolute; top: 70px; left: 80px; width: 120px; height: 6px;
    background: var(--royal);
  }
  .accent-bar--gold { left: 206px; width: 60px; background: var(--gold); }
</style>
</head>
<body>
  <section class="card card--front" aria-label="Business card front">
    <div class="brand">
      <div class="brand__name"><span class="brand__dot"></span>BRIGHTDOOR7</div>
      <div class="brand__tagline">Real estate solution provider</div>
    </div>
    <div class="contact">
      <div class="contact__address">PO Box 4820<br>Cedar Ridge, MD 20999</div>
      <div class="contact__lines">Phone: 555.014.2286<br>Email: info@brightdoor7.example</div>
    </div>
    <div class="site-band">www.brightdoor7.example</div>
    <div class="gold-edge"></div>
  </section>

  <section class="card card--back" aria-label="Business card back">
    <div class="accent-bar"></div>
    <div class="accent-bar accent-bar--gold"></div>
    <div class="services">
      <h2 class="services__title">We specialize in creative real estate solutions</h2>
      <ul class="services__list">
        <li>We pay cash for houses!</li>
        <li>We prevent foreclosures</li>
        <li>We help repair credit!</li>
        <li>We pay referral fees!</li>
      </ul>
    </div>
  </section>
</body>
</html>
```